Menu Design solstane

I need to create a take out menu for my restaurant something nice with some pictures. clean and simple with the colors of my reatsurant. which are orange and black. mostly black.

its fairly simple it has to be 4 pages front cover, inside front menu then 2nd page front and back with menu then 3rd page back front menu, back 3rd sushi menu with specials. final page 4th page, back map with adress and opening hours. and back cover final.

simple elegant and class. black and orange i will send logo and menu as well and pictures.

i am a high end bistro that serves gourmet pizza and pasta. we also have a sushi bar.
the menu will be 6 inches width by 9 inches

the menu that i sent is a pdf file. had an error with word please change font and make a new word dosument.

thank you

• the colors which are black and orange. mostly black.

```html
<!DOCTYPE html>
<html lang="fr">
<head>
<meta charset="utf-8">
<title>Menu Pizza</title>
<link rel="stylesheet" href="https://fonts.googleapis.com/css2?family=Delius+Unicase&family=Open+Sans:ital,wght@1,700&display=swap">
<style>
  :root {
    --page-black: #0c0c0c;
    --page-deep: #050505;
    --swirl-tone: #2a2218;
    --swirl-orange: #3a2a1a;
    --quote-grey: #8d8d8d;
    --menu-white: #f2f2f2;
    --fold-light: #8a8a8a;
    --fold-dark: #4a4a4a;
  }
  * { margin: 0; padding: 0; box-sizing: border-box; }
  html, body { width: 1200px; height: 900px; overflow: hidden; background: var(--page-deep); }
  .spread { position: relative; width: 1200px; height: 900px; }

  .page { position: absolute; top: 0; height: 900px; background: var(--page-black); overflow: hidden; }
  .page--cover { left: 0; width: 590px; }
  .page--menu { left: 610px; width: 590px; }
  .fold { position: absolute; left: 590px; top: 0; width: 20px; height: 900px;
    background: linear-gradient(90deg, var(--fold-dark), var(--fold-light) 45%, var(--fold-light) 55%, var(--fold-dark)); }

  .page-ornament { position: absolute; inset: 0;
    background:
      radial-gradient(ellipse 260px 200px at 30% 18%, var(--swirl-tone), transparent 70%),
      radial-gradient(ellipse 220px 240px at 75% 8%, var(--swirl-orange), transparent 70%),
      radial-gradient(ellipse 300px 220px at 55% 85%, var(--swirl-tone), transparent 70%),
      radial-gradient(ellipse 200px 180px at 15% 70%, #1c1a17, transparent 70%);
    opacity: .7; }

  .quote { position: absolute; font-family: "Open Sans", Arial, sans-serif; font-style: italic; font-weight: 700;
    color: var(--quote-grey); text-align: center; white-space: nowrap; }
  .quote--superb { left: 45px; top: 140px; font-size: 28px; line-height: 42px; letter-spacing: 1.5px; text-align: left; }
  .quote--montreal { left: 222px; top: 337px; width: 363px; font-size: 24px; line-height: 42px; letter-spacing: 0.8px; }
  .quote--soup { left: 27px; top: 615px; width: 440px; font-size: 24px; line-height: 42px; letter-spacing: 0.9px; }

  .menu { position: absolute; inset: 0; font-family: "Delius Unicase", "Comic Sans MS", cursive;
    color: var(--menu-white); font-size: 10px; letter-spacing: -0.4px; text-transform: uppercase; }
  .menu-title { position: absolute; left: 0; width: 643px; top: 24px; text-align: center; font-size: 11px; font-weight: 400; letter-spacing: 0; }
  .line { position: absolute; left: 76px; height: 16px; line-height: 16px; white-space: nowrap; }
  .line--indent { left: 112px; }
  .price { position: absolute; height: 16px; line-height: 16px; letter-spacing: 0; }
  .note { position: absolute; left: 62px; font-size: 7px; line-height: 10px; letter-spacing: 0; white-space: nowrap; }
</style>
</head>
<body>
<main class="spread">
  <section class="page page--cover">
    <div class="page-ornament" role="img" aria-label="Faint dark swirling ornamental flourishes in black and muted orange"></div>
    <p class="quote quote--superb">“A Superb Restaurant...”</p>
    <p class="quote quote--montreal">“...When I am in Montreal I<br>make sure not to miss this<br>restaurant...”</p>
    <p class="quote quote--soup">“...The soup is phenomenal and<br>the dishes are incredibly well<br>prepared.”</p>
  </section>

  <div class="fold"></div>

  <section class="page page--menu">
    <div class="page-ornament" role="img" aria-label="Faint dark swirling ornamental flourishes in black and muted orange"></div>
    <div class="menu">
      <h1 class="menu-title">Pizza</h1>

      <div class="line" style="top:57px">Margarita</div><div class="price" style="left:465px;top:57px">$15.50</div>
      <div class="line" style="top:88px">Sauce tomate, mozzarella &amp; basilic</div>

      <div class="line" style="top:119px">Champignon</div><div class="price" style="left:465px;top:119px">$17.50</div>
      <div class="line line--indent" style="top:138px">Champignon, sauce tomate, mozzarella</div>

      <div class="line" style="top:169px">Trilogie d'olive / olive trilogy</div><div class="price" style="left:467px;top:169px">$17.50</div>
      <div class="line" style="top:189px">Olives, sauce tomate piquante &amp;mozzarella</div>
      <div class="line" style="top:208px">Olives, spicy tomato sauce &amp;mozzarella</div>

      <div class="line" style="top:246px">Vegetarienne / vegetarien</div><div class="price" style="left:468px;top:246px">$18.50</div>
      <div class="line" style="top:266px">Legumes grilles sauce tomato &amp;mozzarella</div>
      <div class="line" style="top:285px">Grilled veggies tomato sauce, mozzarella</div>

      <div class="line" style="top:323px">Pizza d'exception / exception pizza</div><div class="price" style="left:470px;top:323px">$18.50</div>
      <div class="line" style="top:343px">Tomates, sechees, aubergine, olives, sauce, tomates mozzarella</div>
      <div class="line" style="top:362px">Sun dried tomatoes, eggplant, olives, tomato sauce &amp; mozzarella</div>

      <div class="line" style="top:401px">Grecque/greek</div><div class="price" style="left:473px;top:401px">$19.00</div>
      <div class="line" style="top:420px">Feta, olives, oignons rouges, mozzarella, sauce tomate</div>
      <div class="line" style="top:440px">Feta, olives, red onions, mozzarella tomato sauce</div>

      <div class="line" style="top:478px">Thon/tuna</div><div class="price" style="left:473px;top:478px">$18.50</div>
      <div class="line" style="top:498px">Thon, olives, sauce tomate &amp; mozzarella</div>
      <div class="line" style="top:517px">Tuna, olives, tomato sauce &amp; mozzarella</div>

      <div class="line" style="top:555px">Nicoise</div><div class="price" style="left:471px;top:555px">$19.00</div>
      <div class="line" style="top:575px">Anchois, olives, sauce tomate &amp; mozzarella</div>
      <div class="line" style="top:594px">Anchoves, olives mozzarella &amp; tomato sauce</div>

      <div class="line" style="top:632px">Fruit de mar / seafood</div><div class="price" style="left:473px;top:632px">$19.00</div>
      <div class="line" style="top:652px">Crevettes, poireaux, sauce tomate &amp; mozzarella</div>
      <div class="line" style="top:671px">Shrimp, leeks, tomato sauce &amp; mozzarella</div>

      <div class="line" style="top:710px">Calzon</div><div class="price" style="left:472px;top:729px">$ 18.50</div>
      <div class="line" style="top:729px">Poivron rouge, vert &amp; jaune, champignons, oignons,</div>
      <div class="line" style="top:749px">Sauce tomate &amp; mozzarella</div>
      <div class="line" style="top:768px">Red, yellow &amp; green peppers, mushrooms, onions tomato sauce &amp;</div>
      <div class="line" style="top:788px">Mozzarella</div>

      <div class="note" style="top:827px">Toutes nos pizzas sont disponibles sans fromage</div>
      <div class="note" style="top:841px">All our pizzas are avaialble without cheese</div>
      <div class="note" style="top:854px">Ajoutez deux oeufs / add two eggs</div><div class="note" style="left:482px;top:854px">2.95</div>
      <div class="note" style="top:868px">Pate ble entier</div><div class="note" style="left:482px;top:868px">2.25</div>
    </div>
  </section>
</main>
</body>
</html>
```